Großartige Zusammenarbeit. Schnell und absolut zuverlässig. Tolle eigene Idee eingebracht. Trelgrafik hat sich sehr mit dem Projekt beschäftigt und hat den Kern perfekt umgesetzt - besser geht nicht!
Zielgruppe
Wir sind der Lindmoorer Kai Verein. Ein Verein der sich für die Neugestaltung des historischen Hafens in Hamburg-Bergedorf stark macht und Projekte auch in die Tat umsetzt für Bergedorf. Finanziert werden wir durch unsere Mitglieder. Unsere Zielgruppe sind Bergedorfer - Privatleute / Firmen / Einzelhandel in Bergedorf. Menschen die Stolz auf Bergedorf sind und ein Teil dieses Prozessen sein möchten und aktiv Ideen haben, wie man das Hafenareal attraktiver gestalten kann.
Aufgabenstellung
Das Plakat-Projekt, welches es umzusetzen gilt, ist eine Veranstaltung die jährlich stattfindet in dem Kolmwik-Hafen. Der Kolmwik ist der Name des Gewässers. 2017 hat sie bereits stattgefunden. Wir brauchen mehr öffentliche Aufmerksamkeit, wollen hiermit potentielle Mitglieder ansprechen. Das Plakat wird z. B. in dem Markt Galerie Lindmoor aushängen, eventuell auch als digitale Werbung auf den Monitoren im Center geschaltet werden.
Zur Veranstaltung: Es gibt 4 Abende, jeweils spielt eine Live-Band (Rock / Blues / etc.) auf dem Deck eines Bootes der Lindmoorer Fährgesellschaft Musik. Vom Anleger aus verfolgen die Gäste das Event und Getränke gibt es auf dem Boot. Es ist ein Open Air Event. Bilder vom letzten Jahr gibt es auf der Webseite www.lindmoorer-kai.de/Aktuelles
Titel: Klang am Lindmoorer Kai
Text: Unter freiem Himmel als Schwimmbühne im Kolmwik. Bei Schlechtwetter in der Tonkeller im Wendthof
Zusatz: Live und umsonst / Bierverkauf vom Schiff
Textänderungen / weitere Vorschläge sind herzlich willkommen, Hauptsache es gibt einen Bezug zum Hafen und zu Bergedorf.
Hochformat: A2 und Flyer Format z.B. A6 / Übliche digitale Formate JPG / EPS / AI... und MP4 (1080x1920 Pixel 72 DPI)
Inhaltstext zu den Bands die spielen werden:
28.06.2018 / 19 Uhr Velvet Hornets (Blues Rock)
26.07.2018 / 19 Uhr Rusty Pistons ( Rock´n Roll)
30.08.2018 / 19 Uhr The Moorland Pipers ( Schottischer Highland Beat)
27.09.2018 / 19 Uhr Korvidan (Deutscher Rock)

```html
<!DOCTYPE html>
<html lang="de">
<head>
<meta charset="utf-8">
<title>Klang am Lindmoorer Kai</title>
<link rel="stylesheet" href="https://fonts.googleapis.com/css2?family=Londrina+Solid:wght@400;900&family=Raleway:wght@300;400;500&family=Baloo+2:wght@600;700&display=swap">
<style>
  :root {
    --orange: #f7b03a;
    --white: #ffffff;
    --ink: #3a3f45;
    --sky-top: #c9d7d9;
    --sky-mid: #8fa6b4;
    --water: #3e5870;
    --water-deep: #1f3146;
    --mist: #dfe3e6;
    --logo-red: #d7192b;
    --logo-blue: #2f3a8c;
  }
  * { margin: 0; padding: 0; box-sizing: border-box; }
  html, body { width: 855px; height: 1200px; overflow: hidden; background: var(--white); }
  .poster {
    position: relative; width: 855px; height: 1200px; overflow: hidden;
    font-family: "Raleway", sans-serif;
  }
  .backdrop {
    position: absolute; inset: 0;
    background: linear-gradient(180deg, var(--sky-top) 0%, #aebfc6 18%, var(--sky-mid) 32%, #6e8799 45%, var(--water) 58%, #2f465d 70%, var(--water-deep) 100%);
  }
  .keys-art {
    position: absolute; left: 0; top: 820px; width: 855px; height: 380px;
    background: linear-gradient(180deg, rgba(31,49,70,0) 0%, rgba(230,234,238,.55) 40%, var(--mist) 70%, #f4f5f6 100%);
  }
  .tagline {
    position: absolute; left: 0; width: 100%; text-align: center; text-transform: uppercase;
  }
  .tagline--free { top: 32px; color: var(--orange); font-size: 28px; font-weight: 500; letter-spacing: 1px; }
  .tagline--beer { top: 65px; color: var(--ink); font-size: 22px; font-weight: 300; letter-spacing: 1px; }
  .title {
    position: absolute; left: 0; top: 140px; width: 100%; text-align: center;
    font-family: "Londrina Solid", sans-serif; font-weight: 900; line-height: 1;
  }
  .title__main { font-size: 178px; letter-spacing: 2px; }
  .title__am { font-family: "Londrina Solid", sans-serif; font-weight: 400; font-size: 42px; color: var(--orange); vertical-align: 96px; margin-left: 4px; }
  .title__place {
    position: absolute; left: 0; top: 336px; width: 100%; text-align: center;
    font-family: "Londrina Solid", sans-serif; font-weight: 400; font-size: 52px; letter-spacing: 3px;
  }
  .w { color: var(--white); }
  .o { color: var(--orange); }
  .venue {
    position: absolute; left: 0; top: 432px; width: 100%; text-align: center;
    color: #e6ecef; font-size: 12.5px; line-height: 17px; letter-spacing: .6px; text-transform: uppercase;
  }
  .gig {
    position: absolute; width: 380px; text-align: center; font-family: "Baloo 2", sans-serif; line-height: 1;
  }
  .gig__date { color: var(--white); font-size: 24px; font-weight: 700; letter-spacing: 1px; }
  .gig__band { color: var(--white); font-size: 24px; font-weight: 600; margin-top: 10px; }
  .gig__genre { color: var(--orange); font-size: 17px; font-weight: 700; margin-top: 9px; }
  .gig--1 { left: 67px;  top: 562px; }
  .gig--2 { left: 67px;  top: 681px; }
  .gig--3 { left: 430px; top: 562px; }
  .gig--4 { left: 430px; top: 683px; }
  .club-mark {
    position: absolute; left: 36px; top: 992px; width: 281px; height: 104px;
    background: var(--white); display: flex; align-items: center; justify-content: center; gap: 10px;
  }
  .club-mark__square { width: 16px; height: 16px; background: var(--logo-red); }
  .club-mark__name { font-family: "Raleway", sans-serif; font-weight: 500; font-size: 21px; color: var(--logo-blue); }
</style>
</head>
<body>
<main class="poster">
  <div class="backdrop" role="img" aria-label="Unscharfes Foto einer Wasserfläche mit Himmel und Lichtreflexen"></div>
  <div class="keys-art" role="img" aria-label="Grafik aus Klaviertasten, die zu einer Hafen-Skyline aufsteigen"></div>

  <p class="tagline tagline--free">Live und umsonst</p>
  <p class="tagline tagline--beer">Bierverkauf vom Schiff</p>

  <h1 class="title">
    <span class="title__main"><span class="w">K</span><span class="o">LANG</span></span><span class="title__am">AM</span>
  </h1>
  <p class="title__place"><span class="w">LIN</span><span class="o">DM</span><span class="w">OO</span><span class="o">R</span><span class="w">ER K</span><span class="o">A</span><span class="w">I</span></p>

  <p class="venue">Unter freiem Himmel als Schwimmbühne im Kolmwik.<br>Bei Schlechtwetter in der Tonkeller im Wendthof.</p>

  <section class="gig gig--1">
    <p class="gig__date">28.06.2018</p>
    <p class="gig__band">19 Uhr Velvet Hornets</p>
    <p class="gig__genre">(Blues Rock)</p>
  </section>
  <section class="gig gig--2">
    <p class="gig__date">26.07.2018</p>
    <p class="gig__band">19 Uhr Rusty Pistons</p>
    <p class="gig__genre">(Rock´n Roll)</p>
  </section>
  <section class="gig gig--3">
    <p class="gig__date">30.08.2018</p>
    <p class="gig__band">19 Uhr The Moorland Pipers</p>
    <p class="gig__genre">(Schottischer Highland Beat)</p>
  </section>
  <section class="gig gig--4">
    <p class="gig__date">27.09.2018</p>
    <p class="gig__band">19 Uhr Korvidan</p>
    <p class="gig__genre">(Deutscher Rock)</p>
  </section>

  <div class="club-mark">
    <span class="club-mark__square"></span>
    <span class="club-mark__name">Lindmoorer Kai Verein</span>
  </div>
</main>
</body>
</html>
```